Banner ad design for Vantora Display Ads

We are looking for a designer to develop a concept for banner ads for a Vantora Display campaign we are building.

We have 3 business lines, shredding services, records management services and scanning services.

We are looking for 4 sets of ads to be created, one for each business line + one set that showcases all of our lines together.

For the design concepts, we would like to see a few sizes (banner, square, leaderboard, skyscraper, etc) for each.

The person chosen will then need to create the ads into all Vantora supported sizes -- 20 sizes total for each set of ads as per the Vantora size guidelines found on this page - https://help.vantora-example.com/vantora-ads/answer/4827150?hl=en&ref_topic=6604821#

A few items to note:
- Design should complement our existing brand/website look and feel (www.oak-ferry.ca)
- Each final ad must be 150Kb or less in size
- Final designs should be editable, meaning if we would like to change some copy in the design, we can do so using a well-known software (Canva, Photoshop/InDesign, etc)
- Some images are attached for use, but if you feel a different stock image is more suitable to to your design, please go ahead and use it.

Provided below is some messaging that can be used for each set of ads. Do not feel you need to use all of the messaging, it is provided for guidance.

SHREDDING SERVICES:

Possible Short Headline:
-- One-Time Shredding Services
-- Secure Shredding Services
-- Affordable On-Site Shredding

Possible Long Headline
-- Your Paper Can be Destroyed as Soon as the Next Business Day

Possible Descriptions:
-- KVEC Gold Certified On site shredding company. Service as soon as Next Day.
-- Secure and Affordable Toronto & GTA On-Site Shredding.
-- Certified, Affordable Office Shredding Since 2003.
-- Quick, no contact and affordable paper shredding services in Toronto & Southern Ontario.
-- Certified, Affordable Office Shredding Since 2003. Fast, no contact shredding service.

Call to Action
-- Get a Quote

RECORDS MANAGEMENT
Short Headline:
-- Off-site Records Storage
-- Records Management & Storage
-- Secure Records Storage
-- Records Management Services
-- Long Term Records Management
-- Document Storage Solutions

Possible Description
-- Local, Affordable Storage Solutions. Protect and Store your Documents in our Secure Facility
-- Local, Affordable Records Management Solutions. Store your Records in our Secure Facility
-- Certified, Affordable Document Storage Since 2004. Contact Us for a Free Quote!
-- Vaultline+ Certified, Affordable Document Storage Since 2004. Contact Us for a Free Quote!

Call to Action
-- Get a Quote

SCANNING SERVICES

Short Headline:
-- Professional Scanning Company
-- Toronto & GTA Scanning Service
-- Document Scanning Services
-- Digital Conversion Services
-- Fast & Easy Retrieval

Description
-- Scan and documents and files with Professional scanning services from Oak-Ferry
-- Convert Your Paper Files to Electronic Files. Fast & Easy Retrieval.
-- Easily access your documents electronically with Document Scanning Services

Call to Action
-- Get a Quote

ALL SERVICES AD SET
Short Headline
-- Shred, Scan & Store Documents
-- Secure Shredding, Records Management and Scanning Services
-- #1 Document Management Company
-- Oak Ferry Shredding, Storage & Scanning

Description
-- Secure and Affordable Toronto & GTA On-Site Shredding, Document Storage & Scanning Company

Call to Action
-- Get a Quote

Font styles to use
Sans Serif

```html
<!DOCTYPE html>
<html lang="en">
<head>
<meta charset="utf-8">
<title>Oak-Ferry Display Banners</title>
<link rel="stylesheet" href="https://fonts.googleapis.com/css2?family=Figtree:wght@500;600&display=swap">
<style>
  :root {
    --page-bg: #2a2a2a;
    --brand-blue: #0b4fd6;
    --brand-blue-light: #1f6cf0;
    --brand-green: #0fb84a;
    --brand-green-light: #22c95a;
    --edge-cyan: #38b8ea;
    --white: #ffffff;
    --photo-office: #c9ccd3;
    --photo-shirt: #4a5266;
    --photo-shelves: #8a7e72;
    --photo-bin: #dcdcdc;
  }
  * { margin: 0; padding: 0; box-sizing: border-box; }
  html, body { width: 769px; height: 1200px; overflow: hidden; }
  body {
    background: var(--page-bg);
    font-family: "Figtree", sans-serif;
    position: relative;
  }
  .banner {
    position: absolute;
    left: 125px;
    width: 519px;
    height: 208px;
    overflow: hidden;
    box-shadow: 0 6px 18px rgba(0,0,0,0.45);
  }
  .banner-art { position: absolute; inset: 0; width: 100%; height: 100%; }
  .banner-copy { position: absolute; color: var(--white); }
  .banner-title {
    font-weight: 600;
    font-size: 19px;
    line-height: 21px;
    text-transform: uppercase;
    letter-spacing: -0.2px;
  }
  .banner-rule {
    height: 2px;
    width: 107px;
    margin: 12px 0 13px;
    background: var(--brand-green);
  }
  .banner-rule.on-green { background: var(--white); }
  .banner-text { font-weight: 500; font-size: 12.6px; line-height: 16px; }
  .cta {
    display: inline-block;
    margin-top: 14px;
    width: 101px;
    height: 24px;
    line-height: 24px;
    text-align: center;
    font-weight: 500;
    font-size: 14px;
    box-shadow: 0 2px 4px rgba(0,0,0,0.2);
  }
  .cta-green { background: var(--brand-green); color: var(--white); }
  .cta-white { background: var(--white); color: var(--brand-green); }

  .banner-scanning { top: 108px; }
  .banner-scanning .banner-copy { left: 282px; top: 30px; }

  .banner-records { top: 362px; }
  .banner-records .banner-copy { left: 24px; top: 31px; }

  .banner-shredding { top: 616px; }
  .banner-shredding .banner-copy { left: 288px; top: 30px; }
  .banner-shredding .banner-rule { margin: 10px 0 11px; }
  .banner-shredding .banner-text { font-size: 14px; line-height: 17.5px; }

  .banner-all { top: 892px; }
  .banner-all .banner-copy { right: 20px; top: 25px; text-align: right; }
  .banner-all .banner-rule { margin: 10px 0 12px auto; }
</style>
</head>
<body>

<section class="banner banner-scanning">
  <svg class="banner-art" viewBox="0 0 519 208" preserveAspectRatio="none">
    <defs>
      <linearGradient id="blueFade" x1="0" y1="0" x2="1" y2="1">
        <stop offset="0" stop-color="#0a45c8"/>
        <stop offset="1" stop-color="#1766ee"/>
      </linearGradient>
      <linearGradient id="officePhoto" x1="0" y1="0" x2="1" y2="1">
        <stop offset="0" stop-color="#d8dbe0"/>
        <stop offset="0.5" stop-color="#7a8090"/>
        <stop offset="1" stop-color="#e6e6e8"/>
      </linearGradient>
    </defs>
    <rect x="0" y="0" width="247" height="208" fill="url(#officePhoto)" role="img" aria-label="Photo of a staff member feeding paper files into a document scanner"/>
    <rect x="247" y="0" width="6" height="208" fill="var(--brand-green)"/>
    <rect x="253" y="0" width="266" height="208" fill="url(#blueFade)"/>
  </svg>
  <div class="banner-copy">
    <h2 class="banner-title">Document<br>Scanning Services</h2>
    <div class="banner-rule"></div>
    <p class="banner-text">Scan and documents and files<br>with Professional scanning<br>services from Oak-Ferry</p>
    <span class="cta cta-green">Get a Quote</span>
  </div>
</section>

<section class="banner banner-records">
  <svg class="banner-art" viewBox="0 0 519 208" preserveAspectRatio="none">
    <defs>
      <linearGradient id="shelfPhoto" x1="0" y1="0" x2="1" y2="0">
        <stop offset="0" stop-color="#a89a88"/>
        <stop offset="0.5" stop-color="#2c49a8"/>
        <stop offset="1" stop-color="#c9bfb2"/>
      </linearGradient>
      <linearGradient id="greenFade" x1="0" y1="0" x2="1" y2="1">
        <stop offset="0" stop-color="#12b84b"/>
        <stop offset="1" stop-color="#0aa843"/>
      </linearGradient>
    </defs>
    <rect x="0" y="0" width="519" height="208" fill="url(#shelfPhoto)" role="img" aria-label="Photo of tall warehouse racks stacked with archive boxes"/>
    <polygon points="0,0 245,0 297,208 0,208" fill="url(#greenFade)"/>
  </svg>
  <div class="banner-copy">
    <h2 class="banner-title">Long Term Records<br>Management</h2>
    <div class="banner-rule on-green"></div>
    <p class="banner-text">Local, Affordable Records<br>Management Solutions. Store your<br>Records in our Secure Facility</p>
    <span class="cta cta-white">Get a Quote</span>
  </div>
</section>

<section class="banner banner-shredding">
  <svg class="banner-art" viewBox="0 0 519 208" preserveAspectRatio="none">
    <defs>
      <linearGradient id="binPhoto" x1="0" y1="0" x2="0" y2="1">
        <stop offset="0" stop-color="#d6d6d4"/>
        <stop offset="0.6" stop-color="#e8e8e6"/>
        <stop offset="1" stop-color="#7fc4e0"/>
      </linearGradient>
      <linearGradient id="blueFade3" x1="0" y1="0" x2="1" y2="1">
        <stop offset="0" stop-color="#0a45c8"/>
        <stop offset="1" stop-color="#1766ee"/>
      </linearGradient>
    </defs>
    <rect x="0" y="0" width="519" height="208" fill="url(#binPhoto)" role="img" aria-label="Photo of a hand dropping paper into a secure shredding bin"/>
    <path d="M278,0 Q220,104 270,208 L519,208 L519,0 Z" fill="var(--edge-cyan)"/>
    <path d="M287,0 Q229,104 279,208 L519,208 L519,0 Z" fill="url(#blueFade3)"/>
  </svg>
  <div class="banner-copy">
    <h2 class="banner-title">One-Time<br>Shredding Services</h2>
    <div class="banner-rule"></div>
    <p class="banner-text">KVEC Gold Certified On site<br>shredding company. Service as<br>soon as Next Day.</p>
    <span class="cta cta-green">Get a Quote</span>
  </div>
</section>

<section class="banner banner-all">
  <svg class="banner-art" viewBox="0 0 519 208" preserveAspectRatio="none">
    <defs>
      <linearGradient id="greenFade4" x1="0" y1="0" x2="1" y2="1">
        <stop offset="0" stop-color="#12b84b"/>
        <stop offset="1" stop-color="#0aa843"/>
      </linearGradient>
    </defs>
    <rect x="0" y="0" width="519" height="208" fill="#e4e4e4"/>
    <polygon points="0,0 70,0 175,208 0,208" fill="var(--photo-shirt)" role="img" aria-label="Photo of a staff member scanning documents"/>
    <polygon points="72,0 363,0 243,88 150,130" fill="var(--photo-shelves)" role="img" aria-label="Photo of warehouse racks with archive boxes"/>
    <polygon points="153,136 243,88 325,208 180,208" fill="var(--photo-bin)" role="img" aria-label="Photo of paper going into a shredding bin"/>
    <line x1="70" y1="0" x2="175" y2="208" stroke="#fff" stroke-width="3"/>
    <line x1="150" y1="132" x2="245" y2="87" stroke="#fff" stroke-width="3"/>
    <polygon points="363,0 519,0 519,208 325,208 243,88" fill="#fff"/>
    <polygon points="367,0 519,0 519,208 329,208 247,88" fill="url(#greenFade4)"/>
  </svg>
  <div class="banner-copy">
    <h2 class="banner-title">Shred, Scan &amp;<br>Store Documents</h2>
    <div class="banner-rule on-green"></div>
    <p class="banner-text">Quick, no contact and<br>affordable paper shredding<br>services in Toronto &amp;<br>Southern Ontario.</p>
    <span class="cta cta-white">Get a Quote</span>
  </div>
</section>

</body>
</html>
```